Card Design to Advertise New Business

I am looking to have a card designed so that I can pass it out to help promote my business. I have never done this before so I honestly do not know where to start with any ideas. I am providing my website address to help. I provide math tutoring, test prep, and schooling options.

I am looking for a card bigger than a business card but smaller than a flyer. Something front and back that I can pass out.

Business Information
Phone: 470-555-0192
Website: www.kelvanostudyhall.example
Address: 418 Brackenfield Rd Ste 340 Marietta GA 30072
Email: kelvanoservices@kelvanomail.example

Services:
Math Tutoring
NEQ & BOW Test Prep
Group and Private Sessions
Fully Accredited Private School

Target Market(s)

Middle and High School Students

Industry/Entity Type

Education

Requirements
Must have
• Information from my website

```html
<!DOCTYPE html>
<html lang="en">
<head>
<meta charset="utf-8">
<title>Kelvano Study Hall – Promo Card</title>
<link href="https://fonts.googleapis.com/css2?family=Montserrat:wght@500;600;700;800&family=Kalam:wght@700&display=swap" rel="stylesheet">
<style>
:root{
  --page:#dfe4ec;
  --blue:#3f6fd1;
  --red:#d8382b;
  --purple:#6f47b8;
  --purple-dark:#4a2f93;
  --chalk:#2f6e45;
  --wood:#8a5a34;
  --stripe-sky:#6fb4de;
  --stripe-green:#27c22c;
  --stripe-red:#d6391f;
  --stripe-yellow:#d8c51c;
  --white:#ffffff;
}
*{margin:0;padding:0;box-sizing:border-box}
html,body{width:1200px;height:675px;overflow:hidden;background:var(--page)}
body{font-family:"Montserrat",Arial,sans-serif;position:relative}
.promo-card{position:absolute;left:370px;top:37px;width:460px;height:600px;background:var(--white);overflow:hidden;box-shadow:0 6px 20px rgba(0,0,0,.18)}
.hero-photo{position:absolute;left:0;top:0;width:460px;height:260px;background:linear-gradient(135deg,#c9ccd4 0%,#8fb0d8 40%,#e9c9a6 70%,#d9d3c9 100%)}
.headline-banner{position:absolute;left:22px;top:172px;width:420px;height:70px;background:var(--blue);border-radius:12px;transform:rotate(-5deg);color:var(--white);padding:9px 16px;line-height:1.1;white-space:nowrap}
.headline-banner .lead{font-size:16px;font-weight:500;letter-spacing:.2px}
.headline-banner .lead b{font-weight:800}
.headline-banner .main{font-size:25px;font-weight:800;letter-spacing:0}
.tagline-banner{position:absolute;left:24px;top:252px;width:418px;height:30px;background:var(--red);border-radius:12px;transform:rotate(-5deg);color:var(--white);font-size:15px;font-weight:700;padding:5px 14px;white-space:nowrap}
.color-stripes{position:absolute;left:0;top:370px;width:460px;transform:rotate(-2.5deg);transform-origin:left top}
.color-stripes span{display:block;height:14px;width:480px}
.s1{background:var(--stripe-sky)}.s2{background:var(--stripe-green)}.s3{background:var(--stripe-red)}.s4{background:var(--stripe-yellow)}
.contact-band{position:absolute;left:0;top:438px;width:460px;height:200px;background:var(--purple);transform:skewY(-2.5deg);transform-origin:left top}
.rates-badge{position:absolute;left:16px;top:330px;width:165px;height:110px;background:var(--blue);border-radius:22px 40px 26px 34px;transform:rotate(-15deg);color:var(--white);font-family:"Kalam",cursive;font-size:18px;line-height:1.15;text-align:center;padding:14px 8px}
.services-board{position:absolute;left:196px;top:318px;width:250px;height:152px;background:var(--chalk);border:6px solid var(--wood);transform:rotate(-3deg);color:var(--white);padding:10px 12px}
.services-board h2{font-size:20px;font-weight:800;margin-bottom:6px}
.services-board ul{list-style:none;font-size:12.5px;font-weight:600;line-height:1.55}
.services-board li::before{content:"";display:inline-block;width:6px;height:6px;border-radius:50%;background:var(--white);margin-right:6px;vertical-align:middle}
.brand-box{position:absolute;left:16px;top:478px;width:120px;height:112px;background:var(--white);display:flex;flex-direction:column;align-items:center;justify-content:center;gap:8px;text-align:center}
.brand-dot{width:46px;height:46px;border-radius:50%;background:var(--blue)}
.brand-name{font-size:13px;font-weight:700;color:var(--blue);line-height:1.15}
.contact-box{position:absolute;left:148px;top:470px;width:298px;height:120px;background:var(--white);padding:10px 10px;color:var(--purple-dark)}
.contact-row{display:flex;align-items:center;gap:6px;margin-bottom:6px;font-weight:600;font-size:10.5px;white-space:nowrap}
.contact-row.phone{font-size:21px;font-weight:700;margin-bottom:7px}
.contact-row svg{flex:none}
</style>
</head>
<body>
<main class="promo-card">
  <div class="hero-photo" role="img" aria-label="Photo of smiling students writing at classroom desks with a teacher"></div>

  <div class="headline-banner">
    <div class="lead">MORE THAN JUST <b>MATH TUTORING</b></div>
    <div class="main">WE ARE STUDY COACHES</div>
  </div>
  <div class="tagline-banner">Study Coaching and Math Tutoring for all ages</div>

  <div class="color-stripes"><span class="s1"></span><span class="s2"></span><span class="s3"></span><span class="s4"></span></div>
  <div class="contact-band"></div>

  <div class="rates-badge">Lower Rates with Memberships or Packages</div>

  <section class="services-board">
    <h2>Our Services:</h2>
    <ul>
      <li>Math Tutoring</li>
      <li>Group and Private Sessions</li>
      <li>NEQ &amp; BOW Test Prep</li>
      <li>Fully Accredited Private School</li>
    </ul>
  </section>

  <div class="brand-box">
    <div class="brand-dot"></div>
    <div class="brand-name">Kelvano Study Hall</div>
  </div>

  <section class="contact-box">
    <div class="contact-row phone">
      <svg width="20" height="20" viewBox="0 0 20 20"><circle cx="10" cy="10" r="10" fill="#6f47b8"/><path d="M7 5l2 3-1 1.2c.6 1.3 1.5 2.2 2.8 2.8L12 11l3 2-1 2c-4 0-8-4-8-8z" fill="#fff"/></svg>
      470-555-0192
    </div>
    <div class="contact-row">
      <svg width="18" height="18" viewBox="0 0 18 18"><circle cx="9" cy="9" r="9" fill="#6f47b8"/><rect x="4.5" y="6" width="9" height="6.5" fill="none" stroke="#fff" stroke-width="1.2"/><path d="M4.5 6l4.5 3.5L13.5 6" fill="none" stroke="#fff" stroke-width="1.2"/></svg>
      kelvanoservices@kelvanomail.example
    </div>
    <div class="contact-row">
      <svg width="18" height="18" viewBox="0 0 18 18"><circle cx="9" cy="9" r="9" fill="#6f47b8"/><circle cx="9" cy="9" r="4.8" fill="none" stroke="#fff" stroke-width="1.1"/><path d="M4.2 9h9.6M9 4.2c-2.4 2.6-2.4 7 0 9.6M9 4.2c2.4 2.6 2.4 7 0 9.6" fill="none" stroke="#fff" stroke-width="1"/></svg>
      www.kelvanostudyhall.example
    </div>
    <div class="contact-row">
      <svg width="18" height="18" viewBox="0 0 18 18"><circle cx="9" cy="9" r="9" fill="#6f47b8"/><path d="M9 14s-3.5-3.6-3.5-6a3.5 3.5 0 017 0c0 2.4-3.5 6-3.5 6z" fill="none" stroke="#fff" stroke-width="1.2"/><circle cx="9" cy="8" r="1.2" fill="#fff"/></svg>
      418 Brackenfield Rd Ste 340 Marietta GA 30072
    </div>
  </section>
</main>
</body>
</html>
```